Varrow Kestin military/warrior themed clothing company**

eCommerce clothing website

We do have a Shopify account that we would ups like this to be built on for it obvious reasons

We will be starting with the gym/casual wear “Varrow” it will be military style with a unique logo as well as military colours. We will sell this as an exclusive range limited edition to create a scarcity principle which hopefully has our customer desperate to get their gear. We will have it in the colours that Army, Navy and Airforce wear as their undershirts and PT shirts as this will create some great genuine military and KBMQ Security origins. Exclusivity is the key.

Having a similar business model and advertising as LiftOtter who have done incredibly well in this area. Our story is better and we just study what sells and how they sell it. Focused on tops namely shirts and singlet and not 1000 choices keep it simple as simple is best and it sells.

Our story

• Veteran Security Company that requires our staff to keep in shape to provide the community with the best service
• No other brands or designers were up to the task of our military styled training, it all thinned, ripped, and looked terrible
• Decided if it’s broken, fix it and do it ourselves
• Trialed and tested every material and design on the market with extensive hours in the gym, outdoor PT, beach sessions, hill runs, boot camps, go till you puke and we did
• Found what worked and put it into action with a limited order just for our staff
• Some of the boys are still servicing and wore the gear to base PT and their fellow serving members wanted to get some of their own gear to which me made limited orders
• Created purpose PT gear with suitable colour scheme to conform with military regs so the boys no longer got in trouble, made limited orders
• Friends and family really liked the gear so after relentless persistence we gave in and made limited orders
• While performing volunteer advocacy work at the VAFs fellow veterans loved the designs and begged for their own gear which would give them confidence and motivation to get back in the gym to rehabilitate and get their health back, it was a no brainer we made limited order
• We began sponsoring local up and coming athletes, fighters and body builders so they could pursue their dream of becoming a professional in their craft again limited orders were made
• Though more relentless desire to obtain our brand and come onboard with our mission statement influencers and celebrities a like urged to endorse and become brand ambassadors so every Australian could feel what it was like to be apart of a genuine grass roots community that had a great story behind it
• And with that Varrow was born
• Stay tuned for the next exciting instalment of what’s to come as we don’t believe in reinventing the wheel but smashing it down completely

A comprehensive range that targets men and women of all ages, fitness levels, body shapes and their specific needs for all times with an exclusive veterans range to support the veteran community.

Top gym brands
Lift otter
VORN
Pale lantern
Qova
Brelto
Fandry

Target Market(s)

men and women 30-45

Industry/Entity Type

Clothing

Number of Pages Required

5+ page

Font styles to use
Sans Serif

Requirements
Must have
• Home page
• white clean back ground
• menu in the top right corner
• search function
• Varrow lettering up the top nice and clean in black
• crisp Varrow shot of the first shoot in both the black and white gold
• headline "forge your legacy" comes across the bottom of the shot above
• men's lifestyle wear section - pre-order now - hyperlink to casual section
• men's active wear section - pre-order now - hyperlink to fitness section
• women's range - coming soon - hyperlink to women's section
• socials and contact (Facebook, Instagram)

Page 2
• our mission
• our story
• our values

Page 3
Change to lifestyle
Follow the format below for order
Functionality to allow pre-order sales for out of stock units

• men's casual wear
- casual singlets
- casual tees
- casual crews
- casual hoodies
- pre-order now

Page 4
Change to active wear

• men's fitness wear
- fitness tees
- fitness crews
- fitness hoodies
- pre-order now

Page 5
• women's section
- coming soon

Australian owed
Australian made
Australian benefit

Throw in an Australian flag

The whole idea was to be bringing in pre-order sales as we wait for the first order to come in from supplier and the next photo shoot we can simply update all the stock pics as needed. For now I have the tec-pac pics that can go in the product pages.

Mission

Building an unstoppable force of warriors that strive for perfection in every aspect of their lives to forge a legacy

Concept

Varrow is an unstoppable force that protect and inspire their own.

Varrow clothing is battle armour to wear as you take the hardest aspects of life to task.

From our struggle comes our resolve.

Tribute

Our fallen warriors and heroes that have come before us, making the ultimate sacrifice, that has allowed our lives to be free and liberated for an unencumbered pursuit of happiness

Story
• Australian family owned and operated
• Veteran led and staffed
• Created to protect those who protect us
• Tried and tested under military conditions
• Australian sourced and produced
• Ethical and environmentally friendly materials
• Restoration of Australian Pride

Values
• Culture
• Community
• Patriotism
• Honour
• Honesty
• Integrity
• Loyalty
• Courage
• Team work
• Success
Nice to have
• To look and feel like one of the big competitors with ease of navigation and ordering
Should not have
• clutter and loading issues

```html
<!DOCTYPE html>
<html lang="en">
<head>
<meta charset="utf-8">
<title>Varrow — Forge Your Legacy</title>
<link rel="stylesheet" href="https://fonts.googleapis.com/css2?family=Anton&family=Arimo:wght@400;700&display=swap">
<style>
  :root {
    --ink: #0b0b0b;
    --paper: #ffffff;
    --slate: #404a5b;
    --menu-text: #b8bdc7;
    --muted: #6f6f6f;
    --rule: #c9c9c9;
    --hero-dark: #141414;
    --hero-mid: #2c2c2c;
  }
  * { box-sizing: border-box; margin: 0; padding: 0; }
  html, body {
    width: 1200px; height: 815px; overflow: hidden;
    background: var(--paper);
    font-family: "Arimo", Arial, sans-serif;
  }
  .page { position: relative; width: 1200px; height: 815px; overflow: hidden; }

  .brand {
    position: absolute; left: 58px; top: 40px;
    font-size: 62px; font-weight: 400; letter-spacing: 4px;
    color: var(--ink); text-transform: uppercase; line-height: 1;
  }

  .search {
    position: absolute; left: 602px; top: 56px; width: 313px; height: 34px;
    border-bottom: 2px solid var(--rule);
    display: flex; align-items: center; justify-content: space-between;
  }
  .search__label { font-size: 16px; color: var(--muted); }
  .search__icon { width: 42px; height: 20px; margin-right: 4px; }

  .account-bar {
    position: absolute; left: 961px; top: 0; width: 111px; height: 150px;
    background: var(--slate);
  }
  .account-bar svg { position: absolute; left: 39px; }
  .cart-count {
    position: absolute; left: 945px; top: 30px; width: 32px; height: 32px;
    border-radius: 50%; background: var(--paper); border: 1.5px solid var(--ink);
    font-size: 15px; display: flex; align-items: center; justify-content: center;
    color: var(--ink); z-index: 2;
  }

  .menu-close { position: absolute; left: 1118px; top: 50px; width: 38px; height: 38px; }

  .hero {
    position: absolute; left: 0; top: 150px; width: 862px; height: 602px;
    background:
      radial-gradient(ellipse 28% 55% at 58% 55%, #4a4a4a 0%, rgba(60,60,60,0) 100%),
      radial-gradient(ellipse at 50% 40%, var(--hero-mid), var(--hero-dark) 75%);
  }

  .headline-card {
    position: absolute; left: 125px; top: 660px; width: 737px; height: 155px;
    background: var(--paper);
  }
  .headline {
    position: absolute; left: 152px; top: 40px; white-space: nowrap;
    font-family: "Anton", "Arial Narrow", sans-serif;
    font-size: 66px; letter-spacing: 12px; color: var(--ink); line-height: 1;
  }

  .side-menu {
    position: absolute; left: 862px; top: 150px; width: 338px; height: 665px;
    background: var(--slate); z-index: 3;
  }
  .side-menu ul { list-style: none; position: absolute; left: 45px; top: 0; }
  .side-menu li {
    position: absolute; left: 0; white-space: nowrap;
    font-size: 25px; letter-spacing: 2.2px; color: var(--menu-text);
  }
</style>
</head>
<body>
<div class="page">
  <header>
    <div class="brand">Varrow</div>

    <div class="search">
      <span class="search__label">Search our store</span>
      <svg class="search__icon" viewBox="0 0 42 20" aria-hidden="true">
        <g fill="none" stroke="#6f6f6f" stroke-width="3">
          <circle cx="10" cy="11" r="7"/>
          <circle cx="32" cy="11" r="7"/>
          <path d="M17 9h8"/>
        </g>
        <path d="M8 3h5v4H8zM29 3h5v4h-5z" fill="#6f6f6f"/>
      </svg>
    </div>

    <div class="cart-count">3</div>
    <div class="account-bar">
      <svg style="top:26px" width="32" height="38" viewBox="0 0 32 38" aria-label="Bag">
        <g fill="none" stroke="#fff" stroke-width="2.4" stroke-linejoin="round">
          <rect x="3" y="12" width="26" height="24" rx="2"/>
          <path d="M10 17V8a6 6 0 0 1 12 0v9"/>
        </g>
      </svg>
      <svg style="top:96px" width="32" height="34" viewBox="0 0 32 34" aria-label="Account">
        <g fill="none" stroke="#fff" stroke-width="2.6">
          <circle cx="16" cy="9" r="6.5"/>
          <path d="M3 32a13 11 0 0 1 26 0"/>
        </g>
      </svg>
    </div>

    <svg class="menu-close" viewBox="0 0 38 38" aria-label="Close menu">
      <path d="M4 4L34 34M34 4L4 34" stroke="#404a5b" stroke-width="8"/>
    </svg>
  </header>

  <section class="hero" role="img" aria-label="Model in a charcoal brand t-shirt against a dark studio backdrop"></section>

  <div class="headline-card">
    <h1 class="headline">FORGE YOUR LEGACY</h1>
  </div>

  <nav class="side-menu">
    <ul>
      <li style="top:83px">Our Story</li>
      <li style="top:144px">Men Activity Wear</li>
      <li style="top:199px">Men Life Style Wear</li>
      <li style="top:263px">Woman Range</li>
      <li style="top:320px">Cart</li>
      <li style="top:376px">Contact</li>
    </ul>
  </nav>
</div>
</body>
</html>
```